Business Card Design

we specialise in supply of custom uniforms - teamwear to Schools and sporting clubs, see our website: www.kestrelkitworks.com.au, our main corporate colour is black and white, with small amount of gold/yellow

Industry/Entity Type

Business

Contact Information for Business Card

Kestrel Kit Works
Rowan Petrakis
Ph 03 6219 8805
Mobile 0418 262 740
email: rowan@kestrelkitworks.com.au
www.kestrelkitworks.com.au
like us on Pagebook

Requirements
Must have
• modern look & feel

```html
<!DOCTYPE html>
<html lang="en">
<head>
<meta charset="utf-8">
<title>Kestrel Kit Works — Business Card</title>
<link rel="stylesheet" href="https://fonts.googleapis.com/css2?family=Lato:wght@400;700;900&family=Nothing+You+Could+Do&display=swap">
<style>
  :root {
    --backdrop: #2b2b2d;
    --card: #1b1716;
    --white: #f4f4f2;
    --grey: #c9c9c9;
    --gold: #e2bd17;
    --gold-deep: #b99a0e;
    --social-blue: #2f5fae;
  }
  * { box-sizing: border-box; margin: 0; padding: 0; }
  html, body {
    width: 1200px; height: 900px; overflow: hidden;
    background: var(--backdrop);
    font-family: "Lato", Arial, sans-serif;
  }
  .card {
    position: absolute; left: 75px; top: 150px;
    width: 1050px; height: 600px;
    background: var(--card);
    color: var(--white);
  }
  .brand {
    position: absolute; left: 0; right: 0; top: 110px;
    display: flex; align-items: center; justify-content: center; gap: 18px;
  }
  .brand-mark {
    width: 26px; height: 26px; background: var(--gold);
  }
  .brand-name {
    font-weight: 900; font-size: 52px; letter-spacing: 0.5px; color: var(--white);
  }
  .holder {
    position: absolute; left: 110px; top: 300px; width: 340px; text-align: center;
  }
  .holder-name {
    font-weight: 900; font-size: 34px; letter-spacing: 1px; text-transform: uppercase;
  }
  .social {
    margin-top: 34px;
    display: flex; align-items: center; justify-content: center; gap: 12px;
  }
  .social-square { width: 22px; height: 22px; background: var(--social-blue); }
  .social-name { font-weight: 700; font-size: 34px; color: var(--white); }
  .social-cta {
    margin-top: 14px;
    display: flex; align-items: center; justify-content: center; gap: 10px;
  }
  .social-cta svg { width: 52px; height: 34px; }
  .like-us {
    font-family: "Nothing You Could Do", cursive;
    font-size: 26px; color: var(--social-blue);
  }
  .social-handle {
    margin-top: 4px; font-weight: 700; font-size: 26px; color: var(--gold);
  }
  .divider {
    position: absolute; left: 500px; top: 285px;
    width: 3px; height: 230px;
    background: linear-gradient(to bottom, rgba(255,255,255,0), #d8d8d8 55%, #ffffff);
  }
  .contacts {
    position: absolute; left: 545px; top: 300px;
    list-style: none;
  }
  .contact {
    display: flex; align-items: center; gap: 16px;
    font-size: 24px; margin-bottom: 18px; color: var(--white);
  }
  .contact-email { font-size: 21px; color: var(--grey); }
  .icon {
    width: 34px; height: 30px; flex: none;
    background: var(--gold);
    display: flex; align-items: center; justify-content: center;
  }
  .icon svg { width: 22px; height: 20px; }
  .website {
    position: absolute; left: 545px; top: 470px;
    font-weight: 700; font-size: 27px; color: var(--grey);
  }
  .website .www { color: var(--white); }
  .website .domain { color: var(--gold); }
</style>
</head>
<body>
  <main class="card">
    <div class="brand">
      <span class="brand-mark"></span>
      <span class="brand-name">Kestrel Kit Works</span>
    </div>

    <section class="holder">
      <h1 class="holder-name">Rowan Petrakis</h1>
      <div class="social">
        <span class="social-square"></span>
        <span class="social-name">Pagebook</span>
      </div>
      <div class="social-cta">
        <svg viewBox="0 0 52 34" aria-hidden="true">
          <path d="M4 8 C14 2 30 2 36 14" fill="none" stroke="#2f5fae" stroke-width="5" stroke-linecap="round"/>
          <path d="M28 12 L44 12 L36 30 Z" fill="#2f5fae"/>
        </svg>
        <span class="like-us">like us</span>
      </div>
      <p class="social-handle">/kestrelkitworks</p>
    </section>

    <div class="divider"></div>

    <ul class="contacts">
      <li class="contact">
        <span class="icon">
          <svg viewBox="0 0 22 20" aria-hidden="true">
            <rect x="3" y="8" width="16" height="10" rx="2" fill="#1b1716"/>
            <path d="M1 7 Q11 0 21 7 L18 9 L15 6 L7 6 L4 9 Z" fill="#1b1716"/>
          </svg>
        </span>
        03 6219 8805
      </li>
      <li class="contact">
        <span class="icon">
          <svg viewBox="0 0 22 20" aria-hidden="true">
            <rect x="6" y="1" width="10" height="18" rx="2" fill="none" stroke="#1b1716" stroke-width="2"/>
          </svg>
        </span>
        0418 262 740
      </li>
      <li class="contact contact-email">
        <span class="icon">
          <svg viewBox="0 0 22 20" aria-hidden="true">
            <rect x="2" y="4" width="18" height="12" fill="none" stroke="#1b1716" stroke-width="2"/>
            <path d="M2 4 L11 11 L20 4" fill="none" stroke="#1b1716" stroke-width="2"/>
          </svg>
        </span>
        rowan@kestrelkitworks.com.au
      </li>
    </ul>

    <p class="website"><span class="www">www.</span><span class="domain">kestrelkitworks</span>.com.au</p>
  </main>
</body>
</html>
```